Plakat-Design
Zielgruppe
Kosmetikstudio zur Haarentfernung mit Waxing und Sugaring (handwerklich, keine IPL/Lasergeräte).
Angeboten wird die Enthaarung des gesamten Körpers
Am häufigsten gebuchte Behandlung: Brazilian Cut (Enthaarung Intimbereich), gefolgt von Beinen, Achseln und Augenbrauen
Zielgruppe:
Ca. 80% weiblich
Ca. 20% Männer (hauptsächlich Rücken-Enthaarung)
Hauptzielgruppe: 25 bis 35 Jahre, weiblich, interessiert an Schönheit, Mode, Wellness, insgesamt
Werte und Vision:
Spezialisiert: Dadurch, dass wir uns auf eine Sache (im Gegensatz des gesamten Kosmetik-Spektrums) konzentrieren, können wir unseren Kunden einen Service bieten der:
* besonders professionell, schnell, unkompliziert ist und zu einem fairen Preis
Dabei sind für uns folgende Werte besonders wichtig:
* Freundlichkeit, Entspannte Atmosphäre & gutes Miteinander im Team, Professionalität der Service-Qualität
Wir sind das erste Waxing Studio in Trier mit
* >10 Jahren Erfahrung
* > 6.000 zufriedenen Kunden
* > 90.000 professionellen Behandlungen
Mehr Infos auf unserer Website: www.glattora.de
Aufgabenstellung
Zu gestalten sind 5 große Schaufenster. 2 befinden sich an einer Straße, an der Autos vorbei fahren, 3 in der Fußgängerzone. Die Größe der Fenster ist 165x220 cm (BreitexHöhe). Siehe Fotos: Die Größe der Fenster bezieht sich auf jeweils das große Fenster ohne die beiden kleinen Oberlichter.
Wir wünschen uns ein langfristiges Design, das unsere Kunden anspricht und unsere große Werbefläche optimal nutzt.
Wir wünschen uns, dass das Design die oben beschriebene Stimmung vermittelt, unsere langjährige Professionalität, Freundlichkeit, Kundenorientierung, Spaß an der Arbeit/im Studio ....
Wichtig ist auch der Sichtschutz. Da wir körpernah arbeiten und sich hinter den Schaufenstern Kabinen befinden, benötigen wir 100% Sichtschutz. Derzeit sind innenseitig Gardinen angebracht, die Sichtschutz bieten. Die Schaufenstergestaltung könnte zwischen Gardinen und Fenster angebracht werden oder die Gardinen könnten entfernt werden, dann müsste die Schaufenstergestaltung den Sichtschutz bieten.
Die Stadt Trier hat eine Werbesatzung, die einzuhalten ist, ggf. Genehmigung bedarf: https://www.beispielstadt-verwaltung.de/wirtschaft-arbeit/einzelhandel/werbesatzung/
Am einfachsten wäre es, die Werbung innen mit einem Abstand von mind. 10cm zum Fenster anzubringen, um die Werbesatzung zu umgehen. z.B. Banner im Schaufenster. Bei einer Beklebung der Fenster müsste eine Genehmigung angefragt werden.

```html
<!DOCTYPE html>
<html lang="de">
<head>
<meta charset="utf-8">
<title>Glattora – Schaufenster</title>
<link rel="stylesheet" href="https://fonts.googleapis.com/css2?family=Anton&display=swap">
<style>
  :root {
    --wall: #c0a896;
    --frame: #555555;
    --frame-edge: #111111;
    --glass: #eeebe1;
    --poster: #29b8b0;
    --ink: #000000;
    --brand: #ffffff;
  }
  html, body {
    margin: 0;
    padding: 0;
    width: 1200px;
    height: 773px;
    overflow: hidden;
    background: var(--wall);
  }
  .storefront { display: block; width: 1200px; height: 773px; }
  .window-frame { fill: var(--frame); stroke: var(--frame-edge); stroke-width: 2; }
  .window-pane { fill: var(--glass); stroke: var(--frame-edge); stroke-width: 2; }
  .poster { fill: var(--poster); }
  .poster-letter {
    font-family: "Anton", "Oswald", sans-serif;
    fill: var(--ink);
  }
  .brand-name {
    font-family: "Anton", "Oswald", sans-serif;
    fill: var(--brand);
    letter-spacing: 0.5px;
  }
</style>
</head>
<body>
<svg class="storefront" viewBox="0 0 1200 773" xmlns="http://www.w3.org/2000/svg" role="img" aria-label="Drei Schaufenster: We wax you all over – Glattora">
  <defs>
    <g id="window-shell">
      <rect class="window-frame" x="0" y="0" width="293" height="444"/>
      <rect class="window-pane" x="11" y="11" width="132" height="61"/>
      <rect class="window-pane" x="152" y="11" width="131" height="61"/>
      <rect class="window-pane" x="11" y="80" width="272" height="350"/>
      <rect class="poster" x="22" y="99" width="249" height="330"/>
    </g>
  </defs>

  <!-- Fenster 1: WE WAX -->
  <g class="window window--we-wax" transform="translate(87 158)">
    <use href="#window-shell"/>
    <text class="poster-letter" x="30" y="202" font-size="94" textLength="75" lengthAdjust="spacingAndGlyphs">W</text>
    <text class="poster-letter" x="123" y="182" font-size="72" textLength="38" lengthAdjust="spacingAndGlyphs">E</text>
    <text class="poster-letter" x="39" y="324" font-size="70" textLength="51" lengthAdjust="spacingAndGlyphs">W</text>
    <text class="poster-letter" x="80" y="351" font-size="189" textLength="131" lengthAdjust="spacingAndGlyphs">A</text>
    <text class="poster-letter" x="195" y="275" font-size="92" textLength="65" lengthAdjust="spacingAndGlyphs">X</text>
    <text class="brand-name" x="147" y="398" font-size="26" textLength="110" lengthAdjust="spacingAndGlyphs">glattora</text>
  </g>

  <!-- Fenster 2: YOU HIGH PRO -->
  <g class="window window--you" transform="translate(455 158)">
    <use href="#window-shell"/>
    <text class="poster-letter" x="32" y="199" font-size="94" textLength="63" lengthAdjust="spacingAndGlyphs">Y</text>
    <text class="poster-letter" x="85" y="184" font-size="17" textLength="60" lengthAdjust="spacingAndGlyphs">HIGH</text>
    <text class="poster-letter" x="154" y="184" font-size="40" textLength="88" lengthAdjust="spacingAndGlyphs">PRO</text>
    <text class="poster-letter" x="41" y="274" font-size="52" textLength="30" lengthAdjust="spacingAndGlyphs">O</text>
    <text class="poster-letter" x="93" y="354" font-size="191" textLength="109" lengthAdjust="spacingAndGlyphs">U</text>
    <text class="brand-name" x="147" y="398" font-size="26" textLength="110" lengthAdjust="spacingAndGlyphs">glattora</text>
  </g>

  <!-- Fenster 3: ALL OVER -->
  <g class="window window--all-over" transform="translate(824 158)">
    <use href="#window-shell"/>
    <text class="poster-letter" x="29" y="175" font-size="92" textLength="42" lengthAdjust="spacingAndGlyphs">A</text>
    <text class="poster-letter" x="75" y="183" font-size="101" textLength="52" lengthAdjust="spacingAndGlyphs">L</text>
    <text class="poster-letter" x="129" y="174" font-size="91" textLength="50" lengthAdjust="spacingAndGlyphs">L</text>
    <text class="poster-letter" x="39" y="277" font-size="56" textLength="30" lengthAdjust="spacingAndGlyphs">O</text>
    <text class="poster-letter" x="61" y="339" font-size="186" textLength="136" lengthAdjust="spacingAndGlyphs">V</text>
    <text class="poster-letter" x="181" y="326" font-size="72" textLength="86" lengthAdjust="spacingAndGlyphs">ER</text>
    <text class="brand-name" x="147" y="398" font-size="26" textLength="110" lengthAdjust="spacingAndGlyphs">glattora</text>
  </g>
</svg>
</body>
</html>
```